Stationery and Logo Design Project for new NZ Accounting Firm

Our company name is based in Auckland, New Zealand and is called TMV CA Limited. We are a chartered accountancy firm hence the CA abbreviations.

We need a full logo stationery design: Logo, Letterhead, Business Card and Compliments slip.

We are looking for a bold, modern and clean/simple design that makes us stand out. We want to stand out as professionals in the industry and would like the logo and stationery that our clients see to convey this image. We also want to break away from the traditional boring views of book/bean accountants. We are not doing the same old things others are doing and are mainly cloud based but with face to face business relationship focused as well.

We see ourselves as business advisers that provide more than just filing their tax returns. We want to add value to their business and be a partner in their business ventures.

We want the logo to convey the above and also attract potential clients when they see our ads among the thousands on zarvo and the tallow index.

The logo can be for the "TMV" with CA Ltd seperately or a logo/design beside the TMV. But open to other suggestions or concept.

Hi Designers

The designs I have received so far is not quite what I want.

I want something modern and bold that is DIFFERENT from others, from the usual logo designs. Some logo that when people look at it they will remember it as opposed to fading in the background of other competitors' logo.

Lower case lettering for the TMV could be something to explore as I have not seen a lot of these and they do appeal to me.

Thanks

We can focus on the logo first as that will form the main part for all stationery.

Reason: Final stages of choosing a logo design so need to time for designers to submit the letterhead, namecards designs.

Target Market(s)

Our target clients are small to medium business ranging from the sole trader to 50 employees businesses

Industry/Entity Type

Business

```html
<!DOCTYPE html>
<html lang="en">
<head>
<meta charset="utf-8">
<title>TMV CA Limited – Stationery Set</title>
<link rel="stylesheet" href="https://fonts.googleapis.com/css2?family=Arimo:ital,wght@0,400;0,700;1,700&display=swap">
<style>
  :root {
    --page-bg: #ffffff;
    --board: #a7a7a7;
    --paper: #ffffff;
    --brand-red: #8e1f24;
    --ink: #1d1d1d;
    --faint: #e4e4e4;
    --faint-red: #9c3a3e;
    --shadow: rgba(0,0,0,0.35);
  }
  * { box-sizing: border-box; margin: 0; padding: 0; }
  html, body { width: 712px; height: 1200px; overflow: hidden; background: var(--page-bg); }
  body { position: relative; font-family: "Arimo", Arial, sans-serif; color: var(--ink); }

  .board {
    position: absolute; left: 50px; top: 52px; width: 612px; height: 1073px;
    background: var(--board); border-radius: 80px;
  }
  .sheet {
    position: absolute; background: var(--paper); overflow: hidden;
    box-shadow: 2px 3px 5px var(--shadow);
  }
  .card-front { left: 168px; top: 88px; width: 194px; height: 110px; border-radius: 8px; }
  .card-back  { left: 380px; top: 88px; width: 164px; height: 110px; border-radius: 8px; background: var(--brand-red); }
  .letterhead { left: 142px; top: 219px; width: 456px; height: 636px; }
  .compliments { left: 142px; top: 872px; width: 456px; height: 214px; }

  .wordmark {
    display: flex; align-items: center; justify-content: flex-end; gap: 5px;
    font-weight: 700; color: var(--ink); letter-spacing: 0.5px; line-height: 1;
  }
  .wordmark .dot { border-radius: 50%; background: var(--brand-red); flex: none; }
  .tagline { color: var(--brand-red); font-size: 7px; text-align: right; margin-top: 2px; }

  .contact { text-align: right; font-weight: 700; }
  .contact .person { font-weight: 400; color: var(--brand-red); }

  .ghost-mark {
    position: absolute; font-weight: 700; color: var(--faint); line-height: 1;
    letter-spacing: 2px; pointer-events: none;
  }

  /* business card front */
  .card-front .brand { position: absolute; right: 12px; top: 10px; }
  .card-front .wordmark { font-size: 20px; }
  .card-front .wordmark .dot { width: 14px; height: 14px; }
  .card-front .tagline { font-size: 4.5px; }
  .card-front .contact { position: absolute; right: 12px; top: 40px; font-size: 5.5px; line-height: 8.5px; }
  .card-front .contact .person { font-size: 8px; line-height: 10px; }
  .card-front .ghost-mark { left: 4px; top: 20px; font-size: 58px; }

  /* business card back */
  .card-back .ghost-mark { left: 30px; top: 30px; font-size: 44px; color: var(--faint-red); }

  /* letterhead */
  .letterhead .brand { position: absolute; right: 21px; top: 16px; }
  .letterhead .wordmark { font-size: 36px; }
  .letterhead .wordmark .dot { width: 24px; height: 24px; }
  .letterhead .contact { position: absolute; right: 21px; top: 72px; font-size: 8.5px; line-height: 12.6px; }
  .letterhead .contact .person { font-size: 12px; line-height: 14px; }
  .letterhead .ghost-mark { left: 10px; top: 400px; font-size: 130px; }

  /* compliments slip */
  .compliments .greeting {
    position: absolute; left: 22px; top: 14px; font-size: 10px; font-weight: 700;
    font-style: italic; color: var(--brand-red);
  }
  .compliments .brand { position: absolute; right: 21px; top: 16px; }
  .compliments .wordmark { font-size: 36px; }
  .compliments .wordmark .dot { width: 24px; height: 24px; }
  .compliments .contact { position: absolute; right: 21px; top: 72px; font-size: 8.5px; line-height: 12.6px; }
  .compliments .contact .person { font-size: 12px; line-height: 14px; }
  .compliments .ghost-mark { left: 100px; top: 60px; font-size: 100px; }
</style>
</head>
<body>
  <div class="board"></div>

  <section class="sheet card-front" aria-label="Business card front">
    <div class="ghost-mark" aria-hidden="true">TMV</div>
    <div class="brand">
      <div class="wordmark"><span class="dot"></span>TMV</div>
      <div class="tagline">Chartered Accountancy Ltd.</div>
    </div>
    <address class="contact" style="font-style:normal">
      <div class="person">Daniel Hart</div>
      <div>Street, Region, Country</div>
      <div>PO BOX 785</div>
      <div>+64 (9) 210 4471</div>
      <div>+64 (21) 655 903</div>
      <div>hello@tmvadvisory.nz</div>
      <div>www.tmvadvisory.nz</div>
    </address>
  </section>

  <section class="sheet card-back" aria-label="Business card back">
    <div class="ghost-mark" aria-hidden="true">TMV</div>
  </section>

  <section class="sheet letterhead" aria-label="Letterhead">
    <div class="ghost-mark" aria-hidden="true">TMV</div>
    <div class="brand">
      <div class="wordmark"><span class="dot"></span>TMV</div>
      <div class="tagline">Chartered Accountancy Ltd.</div>
    </div>
    <address class="contact" style="font-style:normal">
      <div class="person">Daniel Hart</div>
      <div>Street, Region, Country</div>
      <div>PO BOX 785</div>
      <div>+64 (9) 210 4471</div>
      <div>+64 (21) 655 903</div>
      <div>hello@tmvadvisory.nz</div>
      <div>www.tmvadvisory.nz</div>
    </address>
  </section>

  <section class="sheet compliments" aria-label="Compliments slip">
    <div class="ghost-mark" aria-hidden="true">TMV</div>
    <div class="greeting">With Compliments</div>
    <div class="brand">
      <div class="wordmark"><span class="dot"></span>TMV</div>
      <div class="tagline">Chartered Accountancy Ltd.</div>
    </div>
    <address class="contact" style="font-style:normal">
      <div class="person">Daniel Hart</div>
      <div>Street, Region, Country</div>
      <div>PO BOX 785</div>
      <div>+64 (9) 210 4471</div>
      <div>+64 (21) 655 903</div>
      <div>hello@tmvadvisory.nz</div>
      <div>www.tmvadvisory.nz</div>
    </address>
  </section>
</body>
</html>
```